Concept design for a tea business Labels

Hello, we are looking for concepts for our label/packaging for a tea business that has been in business now for over a year. We are a beachy, organic, "It's your moment. Enjoy it." type tea business. We have an online website (www.driftleafbrews.com.au) and sell at local markets around the Corvel Cove area.
We are looking to upgrade our label to look more professional, in a fun/beachy/chilled out style. (unlike the traditional tea labels).
We do loose leaf tea and iced tea consentrated syrups. We have a few different packages (please see website under "sizes and packaging" bottom left). We would like to experiement with various different size and shape of labels for different products, so would like a concept design for a label using our logo (see website front page bottom). There are no colour constraints.
We use the Norvik brand labels of the following sizes:
1. Pure Glint Rectangular Product Labels, Q4826, 100/Pack, 96 x 50.8 mm
2. Pure Glint Round Multi-purpose Labels, Q3957D, 240/Pack, 40 mm diameter
3.Pure Glint Square Product Labels, Q4861, 350/Pack, 35 x 35 mm
4. For bottles we use Grained Ivory Domed Labels, Q4839, 90/Pack, 57.2 x 77 mm
If you have any more questions, please don't hesitate to contact me
Updates
Hi All,
I am considering using a box like below for packing and doing a bit of a white/beachy feel to the packaging. Either using the rectangle or round circle labels. (circle labels from norvik 60mm diameter).

Reason: Hi All - Thank you so much for all your designs. While I have seen some really beautiful designs I am excited about, it seems there was a rush at the end with a number of new designs just submitted. I still haven't seen just one design I love for the label, so I would like the opportunity to work with some of the new designers to see if we can modify to suit the concept.
Would anyone like to try a concept label with a silhouette of one of the following wave/beach/teacup? I'm just exploring a different approach as I know it is difficult tying in the beach with tea - please think - chilled out beach hut with tea/iced tea, sunrise over ocean. I like the soft colour palette - beachy feel to it - ie. Pastels - blues, greens, whites, sandy, pinks, purples, greys - sunrises over ocean, maybe a white rustic wood feel - or any other icon from Corvel Cove - like the Norfolk Pine's along the beach - maybe in Silhouette.
Just some more ideas.
Thank you again for all your contributions!
Greta

```html
<!DOCTYPE html>
<html lang="en">
<head>
<meta charset="utf-8">
<title>Corvel Tea Company – Product Labels</title>
<link href="https://fonts.googleapis.com/css2?family=Arimo:wght@400;700&family=PT+Sans&display=swap" rel="stylesheet">
<style>
  :root {
    --page-bg: #ffffff;
    --brand-orange: #f15a2b;
    --ink-white: #ffffff;
    --caption-ink: #333333;
    --white-top: #dcd3cd;
    --white-bottom: #957c6e;
    --white-bar: #6d6259;
    --black-top: #6a6a6c;
    --black-bottom: #221e1f;
    --black-bar: #414143;
    --green-top: #a3cd3a;
    --green-bottom: #0c9447;
    --green-bar: #3bb54a;
    --rooibos-top: #d38e2c;
    --rooibos-bottom: #a3571d;
    --rooibos-bar: #e19a36;
    --art-light: rgba(246, 242, 236, 0.78);
    --art-warm: rgba(226, 170, 110, 0.55);
  }
  html, body {
    margin: 0;
    padding: 0;
    width: 1200px;
    height: 587px;
    overflow: hidden;
    background: var(--page-bg);
    font-family: "Arimo", Arial, sans-serif;
  }
  .sheet {
    position: relative;
    width: 1200px;
    height: 587px;
  }
  .label {
    position: absolute;
    top: 33px;
    width: 246px;
    height: 464px;
    border-radius: 14px;
    overflow: hidden;
  }
  .label--white   { left: 49px;  background: linear-gradient(180deg, var(--white-top), var(--white-bottom)); }
  .label--black   { left: 337px; background: linear-gradient(180deg, var(--black-top), var(--black-bottom)); }
  .label--green   { left: 623px; background: linear-gradient(180deg, var(--green-top), var(--green-bottom)); }
  .label--rooibos { left: 905px; background: linear-gradient(180deg, var(--rooibos-top), var(--rooibos-bottom)); }

  .brand-name {
    position: absolute;
    left: 20px;
    top: 0;
    width: 206px;
    height: 58px;
    background: var(--brand-orange);
    color: var(--ink-white);
    font-weight: 700;
    font-size: 21px;
    line-height: 58px;
    text-align: center;
    letter-spacing: -0.3px;
    z-index: 1;
  }
  .cup-art {
    position: absolute;
    left: 24px;
    top: 58px;
    width: 206px;
    height: 218px;
    background: linear-gradient(160deg, var(--art-light), var(--art-warm));
  }
  .variety {
    position: absolute;
    left: 25px;
    top: 347px;
    width: 200px;
    height: 44px;
    color: var(--ink-white);
    font-weight: 700;
    font-size: 18px;
    line-height: 44px;
    text-align: center;
  }
  .label--white .variety   { background: var(--white-bar); }
  .label--black .variety   { background: var(--black-bar); }
  .label--green .variety   { background: var(--green-bar); left: 23px; }
  .label--rooibos .variety { background: var(--rooibos-bar); left: 21px; }

  .tagline {
    position: absolute;
    left: 0;
    top: 407px;
    width: 246px;
    margin: 0;
    color: var(--ink-white);
    font-weight: 700;
    font-size: 22px;
    line-height: 24px;
    text-align: center;
    letter-spacing: -0.3px;
  }
  .caption {
    position: absolute;
    left: 0;
    top: 545px;
    width: 1200px;
    margin: 0;
    color: var(--caption-ink);
    font-family: "PT Sans", Arial, sans-serif;
    font-size: 17px;
    line-height: 22px;
    text-align: center;
  }
</style>
</head>
<body>
<main class="sheet">
  <section class="label label--white">
    <div class="brand-name">Corvel Tea Company</div>
    <div class="cup-art" role="img" aria-label="Photo: cup of tea on a saucer with a spoon and fresh tea leaves, seen from above"></div>
    <div class="variety">WHITE TEA</div>
    <p class="tagline">It’s your moment.<br>Enjoy It.</p>
  </section>

  <section class="label label--black">
    <div class="brand-name">Corvel Tea Company</div>
    <div class="cup-art" role="img" aria-label="Photo: cup of tea on a saucer with a spoon and fresh tea leaves, seen from above"></div>
    <div class="variety">BLACK TEA</div>
    <p class="tagline">It’s your moment.<br>Enjoy It.</p>
  </section>

  <section class="label label--green">
    <div class="brand-name">Corvel Tea Company</div>
    <div class="cup-art" role="img" aria-label="Photo: cup of tea on a saucer with a spoon and fresh tea leaves, seen from above"></div>
    <div class="variety">GREEN TEA</div>
    <p class="tagline">It’s your moment.<br>Enjoy It.</p>
  </section>

  <section class="label label--rooibos">
    <div class="brand-name">Corvel Tea Company</div>
    <div class="cup-art" role="img" aria-label="Photo: cup of tea on a saucer with a spoon and fresh tea leaves, seen from above"></div>
    <div class="variety">ROOIBOS TEA</div>
    <p class="tagline">It’s your moment.<br>Enjoy It.</p>
  </section>

  <p class="caption">Pure Glint Rectangular Product Labels, Q4826, 100/Pack, 96 x 50.8 mm</p>
</main>
</body>
</html>
```